UI Mockup For Online Scheduling Software

11.01.2018 - Brief Update:
The brief has not changed but the summary below as being added to aid designers.

- New file added "Updated 11.01.2018 - Individual Box" to clarify the sections. Specifically the primary tag section
- Improve on the current styling
- Consider changing the section layout to maximise the number of blocks displayed on screen (The sections dont not need to be stacked like the current version.
- The design is for the application running on a desktop PC with 16:9 screen aspect
- The design styling/layout should not look like the current version
- You may use the application to get an understanding of its workings at this link....https://tomsbrevik.lqnhosting.com.au/
- Think outside the box....use your creative flare and show me something different to the current app (style and layout)

There are already some good submissions so closer to the deadline I will increase the budget and award $$$ to 1st and 2nd. The winner will be chosen to directly work on the remaining aspects of this application (setting page, mobile design, dashboard etc). The next design project associated to this application will be 10 time bigger than this one.

Good Luck Designers

*************************************************************
Redesign the user interface to make more efficient use of the screen real estate.

The software works by adding (Drag & Drop) Project Blocks to a Date Section. Then tags are added (Drag & Drop) to the block section below the header, and then resources are added to the block section below the tags.
Each block has 4 main sections that are stacked vertically:

1. Header - Displays Title and Address
2. Tags - Displays tags, maximum of 6 tags
3. Resources - Displays resources, maximum of 10 resources, NOTE: this section can be hidded.
4. Footer - Display basic stats (eg. 3 Resources assigned)

It is critical that as many block (20-30) as possible for a single date can be visible on screen.

The following criteria must be considered when mocking up layout:
1. Font Type, size, colour and emphasis
2. Block Colour/Shading, borders ect
3. Section Layout within the block (stacking & Alignment)
4. Mock ups to show scaled layout of blocks in both the open state and Closed State.
5. Mock up to display a minimum of 20 blocks.
6. Create a variation of your design that adds a 5th section. This will display the first tag only:
1. Header - Always Visible
2. Primary Tag - Always Visible
3. Secondary Tags - Can be hidden
4. Resources - Can be Hidden
5. Footer - Can be Hidden

Please be creative with your design and layout. I like a clean, minimalist design.
At this stage CSS file will not be required but would be benificial

Target Market(s)

N/A

Industry/Entity Type

Software

Number of Pages Required

1 page

Font styles to use
Other font styles liked:
• Designers Choice

Colors

Designer to choose colors to be used in the design.

Requirements
Must have
• Variation to current layout and style
Should not have
• Same styling and layout as current design

```html
<!DOCTYPE html>
<html lang="en">
<head>
<meta charset="utf-8">
<title>Gunmix Australia – Scheduler</title>
<link href="https://fonts.googleapis.com/css2?family=Inter:wght@400;500;600&display=swap" rel="stylesheet">
<style>
:root{
  --navy:#23242f;
  --side:#2a2b37;
  --side-top:#343540;
  --teal:#1aaa8e;
  --teal-light:#21c4a5;
  --sky:#cfe8f3;
  --sky-dark:#c2e0ec;
  --col:#e8e8ea;
  --main:#f0f0f2;
  --white:#ffffff;
  --ink:#2a2b33;
  --muted:#9a9ba3;
  --red:#e0312b;
  --line:#e4e4e8;
}
*{box-sizing:border-box;margin:0;padding:0}
html,body{width:1200px;height:1200px;overflow:hidden}
body{font-family:"Inter",sans-serif;color:var(--ink);background:var(--main);position:relative}
svg{display:block}

.topbar{position:absolute;left:0;top:0;width:1200px;height:42px;background:var(--navy)}
.brand{position:absolute;left:18px;top:13px;color:var(--white);font-size:12px;font-weight:500;letter-spacing:.3px}
.welcome{position:absolute;right:0;top:0;width:106px;height:42px;background:#2c2d39;color:#dcdce0;font-size:10px;display:flex;align-items:center;justify-content:center;gap:10px}
.welcome .dot{width:15px;height:15px;border-radius:50%;background:var(--teal-light);display:flex;align-items:center;justify-content:center}

.sidebar{position:absolute;left:0;top:42px;width:168px;height:1158px;background:var(--side)}
.sidebar .dash{height:101px;background:var(--side-top);position:relative}
.nav-item{position:absolute;left:0;width:168px;height:20px;display:flex;align-items:center;color:var(--white);font-size:10px;letter-spacing:.2px}
.nav-item .ico{position:absolute;left:12px;color:var(--teal-light)}
.nav-item .lbl{position:absolute;left:36px}
.nav-item .chev{position:absolute;left:134px;width:16px;height:16px;border:1.3px solid var(--teal-light);border-radius:50%;display:flex;align-items:center;justify-content:center}
.sub{position:absolute;left:48px;font-size:7px;color:#c9c9cf}
.sub.active{color:var(--teal-light);border-left:1px solid var(--teal-light);padding-left:7px;left:40px}

.panel{position:absolute;left:168px;top:42px;width:164px;height:1158px;background:var(--col)}
.show-btn{position:absolute;left:4px;top:5px;width:158px;height:35px;background:var(--teal);color:var(--white);font-size:10px;display:flex;align-items:center;justify-content:center;border-radius:2px;box-shadow:0 1px 3px rgba(0,0,0,.2)}
.acc{position:absolute;left:4px;width:157px;height:21px;background:var(--white);font-size:8px;display:flex;align-items:center;padding-left:28px}
.acc span{color:var(--muted);margin-left:3px}
.acc svg{position:absolute;left:8px}
.acc.open{background:var(--sky)}
.acc.open span{color:var(--teal)}
.tags-panel{position:absolute;left:4px;top:148px;width:157px;height:648px;background:var(--sky);overflow:hidden}
.search{position:absolute;left:6px;top:6px;width:146px;height:28px;background:var(--white);font-size:8px;padding:10px 11px}
.tag-list{position:absolute;left:6px;top:44px;width:136px}
.group{height:30px;background:var(--sky-dark);font-size:8px;display:flex;align-items:center;padding-left:11px;margin:6px 0 7px}
.day{height:15px;background:var(--white);font-size:5.5px;display:flex;align-items:center;padding-left:21px;margin-bottom:4.5px;position:relative;width:134px}
.day svg{position:absolute;left:8px}
.scroll{position:absolute;left:148px;top:44px;width:2px;height:556px;background:#b7d3df}
.scroll i{position:absolute;left:0;top:14px;width:2px;height:250px;background:var(--navy)}

.filters{position:absolute;left:332px;top:42px;width:868px;height:73px;background:var(--sky)}
.filters .title{position:absolute;left:21px;top:30px;font-size:10px}
.field{position:absolute;top:21px;height:29px;background:var(--white);font-size:6.5px;display:flex;align-items:center;padding-left:6px}
.field svg{position:absolute;right:6px}
.btn{position:absolute;top:21px;height:29px;background:var(--teal-light);color:var(--white);font-size:8px;display:flex;align-items:center;justify-content:center;border-radius:3px;box-shadow:0 1px 3px rgba(0,0,0,.2)}
.tabs{position:absolute;left:332px;top:115px;width:868px;height:28px;background:var(--sky-dark)}
.tab{position:absolute;top:0;height:28px;background:var(--sky);font-size:8px;color:#f4fafd;display:flex;align-items:center;justify-content:center}
.tab.active{color:var(--ink)}
.dateline{position:absolute;left:332px;top:143px;width:868px;height:30px;background:var(--white)}
.dateline .day-label{position:absolute;left:30px;top:10px;font-size:9.5px}
.dateline .day-label small{font-size:6px;color:var(--teal)}
.comment{position:absolute;left:560px;top:2px;width:68px;height:27px;background:var(--teal);color:var(--white);font-size:7px;display:flex;align-items:center;justify-content:center;gap:5px}
.stat{position:absolute;top:12px;font-size:6.5px;color:var(--teal)}

.board{position:absolute;left:346px;top:187px;display:grid;grid-template-columns:repeat(4,196px);column-gap:18.4px;row-gap:18px}
.block{width:196px;height:90px;background:var(--white);border-radius:3px;overflow:hidden;box-shadow:0 1px 2px rgba(0,0,0,.05)}
.block-head{height:30px;background:var(--navy);color:var(--white);position:relative;text-align:center;padding-top:5px}
.block-head h3{font-size:9.5px;font-weight:400;letter-spacing:.1px;margin-left:-12px}
.block-head .addr{font-size:4px;color:#c5c6cc;margin-top:3px;margin-left:-12px}
.block-head .gear{position:absolute;right:11px;top:10px}
.tag{margin:8px 17px 0;height:19px;background:var(--sky);display:flex;align-items:center;padding-left:6px;position:relative;font-size:5px}
.tag span{margin-left:5px}
.tag .x{position:absolute;right:6px}
.block-foot{border-top:1px solid var(--line);margin-top:8px;height:24px;display:flex;align-items:center;justify-content:space-between;padding:0 28px 0 27px}
</style>
</head>
<body>
<svg width="0" height="0" style="position:absolute">
  <defs>
    <symbol id="i-gear" viewBox="0 0 20 20"><circle cx="10" cy="10" r="6.5" fill="none" stroke="#fff" stroke-width="1.6" stroke-dasharray="3 1.6"/><circle cx="10" cy="10" r="2.8" fill="none" stroke="#fff" stroke-width="1.4"/></symbol>
    <symbol id="i-tag" viewBox="0 0 20 20"><circle cx="10" cy="10" r="8.5" fill="none" stroke="#23242f" stroke-width="1.6"/><path d="M6 6h4.5l4 4-4.5 4.5-4-4z" fill="#23242f"/></symbol>
    <symbol id="i-x" viewBox="0 0 10 10"><path d="M2 2l6 6M8 2l-6 6" stroke="#e0312b" stroke-width="2.2"/></symbol>
    <symbol id="i-user" viewBox="0 0 20 20"><circle cx="10" cy="6" r="4" fill="#23242f"/><path d="M2 19c1-5 4-7 8-7s7 2 8 7z" fill="#23242f"/><circle cx="5" cy="3" r="2.4" fill="#1aaa8e"/></symbol>
    <symbol id="i-doc" viewBox="0 0 20 20"><rect x="6" y="5" width="11" height="13" fill="#bfc0c6"/><path d="M8 9h7M8 12h7M8 15h5" stroke="#fff" stroke-width="1"/><circle cx="5" cy="4" r="2.6" fill="#8fd0e6"/></symbol>
    <symbol id="i-chart" viewBox="0 0 20 20"><path d="M3 18h15" stroke="#c7c8cd" stroke-width="1.2"/><rect x="4" y="12" width="2.5" height="6" fill="#c7c8cd"/><rect x="8" y="9" width="2.5" height="9" fill="#c7c8cd"/><rect x="12" y="6" width="2.5" height="12" fill="#c7c8cd"/><path d="M3 12l5-4 4 2 6-6" stroke="#c7c8cd" stroke-width="1.2" fill="none"/></symbol>
    <symbol id="i-right" viewBox="0 0 10 10"><path d="M3 1.5L6.5 5 3 8.5" stroke="#2a2b33" stroke-width="1.6" fill="none"/></symbol>
    <symbol id="i-down" viewBox="0 0 10 10"><path d="M1.5 3L5 6.5 8.5 3" stroke="#2a2b33" stroke-width="1.6" fill="none"/></symbol>
    <symbol id="i-down-teal" viewBox="0 0 10 10"><path d="M1.5 3L5 6.5 8.5 3" stroke="#21c4a5" stroke-width="1.6" fill="none"/></symbol>
    <symbol id="i-label" viewBox="0 0 10 10"><path d="M1 1h4.5L9 4.5 4.5 9 1 5.5z" fill="#23242f"/></symbol>
    <symbol id="i-list" viewBox="0 0 12 12"><path d="M0 1.5h2M0 4.5h2M0 7.5h2M0 10.5h2M3.5 1.5h8.5M3.5 4.5h8.5M3.5 7.5h8.5M3.5 10.5h8.5" stroke="currentColor" stroke-width="1.8"/></symbol>
  </defs>
</svg>

<header class="topbar">
  <div class="brand">Gunmix Australia</div>
  <div class="welcome">Welcome <span class="dot"><svg width="9" height="9" viewBox="0 0 10 10"><path d="M2 3.5L5 6.5 8 3.5" stroke="#23242f" stroke-width="1.8" fill="none"/></svg></span></div>
</header>

<nav class="sidebar">
  <div class="dash">
    <div class="nav-item" style="top:6px"><svg class="ico" width="16" height="12" viewBox="0 0 16 12"><path d="M1 2l3 9h8l3-9-4 2-3-3-3 3z" fill="#fff"/></svg><span class="lbl">DASHBOARD</span><span class="chev"><svg width="8" height="8" viewBox="0 0 10 10"><path d="M1.5 6.5L5 3l3.5 3.5" stroke="#21c4a5" stroke-width="1.6" fill="none"/></svg></span></div>
    <div class="sub active" style="top:36px">Lorem Ipsum</div>
    <div class="sub" style="top:56px">Dummy text of the</div>
    <div class="sub" style="top:75px">Lorem is simply</div>
  </div>
  <div class="nav-item" style="top:121px"><svg class="ico" width="14" height="12" viewBox="0 0 14 12"><rect x="0.5" y="0.5" width="13" height="8" fill="none" stroke="#21c4a5" stroke-width="1.4"/><path d="M4 11.5h6M7 9v2.5" stroke="#21c4a5" stroke-width="1.4"/></svg><span class="lbl">PROJECTS</span><span class="chev"><svg width="8" height="8"><use href="#i-down-teal"/></svg></span></div>
  <div class="nav-item" style="top:158px"><svg class="ico" width="12" height="12"><use href="#i-list"/></svg><span class="lbl">RESOURCES</span><span class="chev"><svg width="8" height="8"><use href="#i-down-teal"/></svg></span></div>
  <div class="nav-item" style="top:196px"><svg class="ico" width="12" height="12"><use href="#i-list"/></svg><span class="lbl">PLANTS</span><span class="chev"><svg width="8" height="8"><use href="#i-down-teal"/></svg></span></div>
  <div class="nav-item" style="top:233px"><svg class="ico" width="12" height="12"><use href="#i-list"/></svg><span class="lbl">TAGS</span><span class="chev"><svg width="8" height="8"><use href="#i-down-teal"/></svg></span></div>
  <div class="nav-item" style="top:270px"><svg class="ico" width="12" height="12"><use href="#i-list"/></svg><span class="lbl">CLIENTS</span><span class="chev"><svg width="8" height="8"><use href="#i-down-teal"/></svg></span></div>
</nav>

<aside class="panel">
  <div class="show-btn">SHOW</div>
  <div class="acc" style="top:47px"><svg width="8" height="8"><use href="#i-right"/></svg>Project list <span>(67)</span></div>
  <div class="acc" style="top:73px"><svg width="8" height="8"><use href="#i-right"/></svg>Resource <span>(55)</span></div>
  <div class="acc" style="top:100px"><svg width="8" height="8"><use href="#i-right"/></svg>Plant <span>(25)</span></div>
  <div class="acc open" style="top:127px"><svg width="8" height="8"><use href="#i-down"/></svg>Project Tags <span>(115)</span></div>
  <div class="tags-panel">
    <div class="search">Seach for...</div>
    <div class="tag-list">
      <div class="group">1.1 Not Working</div>
      <div class="day"><svg width="6" height="6"><use href="#i-label"/></svg>Day Booked Off</div>
      <div class="day"><svg width="6" height="6"><use href="#i-label"/></svg>Day Booked Off</div>
      <div class="group">1.0 Trades</div>
      <div class="day"><svg width="6" height="6"><use href="#i-label"/></svg>Day Booked Off</div>
      <div class="day"><svg width="6" height="6"><use href="#i-label"/></svg>Day Booked Off</div>
      <div class="day"><svg width="6" height="6"><use href="#i-label"/></svg>Day Booked Off</div>
      <div class="day"><svg width="6" height="6"><use href="#i-label"/></svg>Day Booked Off</div>
      <div class="day"><svg width="6" height="6"><use href="#i-label"/></svg>Day Booked Off</div>
      <div class="day"><svg width="6" height="6"><use href="#i-label"/></svg>Day Booked Off</div>
      <div class="day"><svg width="6" height="6"><use href="#i-label"/></svg>Day Booked Off</div>
      <div class="group">2.1 Task - Steel/shot</div>
      <div class="day"><svg width="6" height="6"><use href="#i-label"/></svg>Day Booked Off</div>
      <div class="day"><svg width="6" height="6"><use href="#i-label"/></svg>Day Booked Off</div>
      <div class="day"><svg width="6" height="6"><use href="#i-label"/></svg>Day Booked Off</div>
      <div class="day"><svg width="6" height="6"><use href="#i-label"/></svg>Day Booked Off</div>
      <div class="day"><svg width="6" height="6"><use href="#i-label"/></svg>Day Booked Off</div>
      <div class="day"><svg width="6" height="6"><use href="#i-label"/></svg>Day Booked Off</div>
      <div class="day"><svg width="6" height="6"><use href="#i-label"/></svg>Day Booked Off</div>
      <div class="day"><svg width="6" height="6"><use href="#i-label"/></svg>Day Booked Off</div>
      <div class="day"><svg width="6" height="6"><use href="#i-label"/></svg>Day Booked Off</div>
      <div class="day"><svg width="6" height="6"><use href="#i-label"/></svg>Day Booked Off</div>
      <div class="day"><svg width="6" height="6"><use href="#i-label"/></svg>Day Booked Off</div>
      <div class="day"><svg width="6" height="6"><use href="#i-label"/></svg>Day Booked Off</div>
      <div class="day"><svg width="6" height="6"><use href="#i-label"/></svg>Day Booked Off</div>
      <div class="day"><svg width="6" height="6"><use href="#i-label"/></svg>Day Booked Off</div>
    </div>
    <div class="scroll"><i></i></div>
  </div>
  <div class="acc" style="top:766px"><svg width="8" height="8"><use href="#i-right"/></svg>Project list <span>(67)</span></div>
  <div class="acc" style="top:793px"><svg width="8" height="8"><use href="#i-right"/></svg>Resource <span>(55)</span></div>
  <div class="acc" style="top:819px"><svg width="8" height="8"><use href="#i-right"/></svg>Plant <span>(25)</span></div>
  <div class="acc" style="top:846px"><svg width="8" height="8"><use href="#i-right"/></svg>Project list <span>(67)</span></div>
  <div class="acc" style="top:873px"><svg width="8" height="8"><use href="#i-right"/></svg>Resource <span>(55)</span></div>
  <div class="acc" style="top:899px"><svg width="8" height="8"><use href="#i-right"/></svg>Plant <span>(25)</span></div>
</aside>

<section class="filters">
  <div class="title">Filter By Date</div>
  <div class="field" style="left:94px;width:145px">10-01-2018</div>
  <div class="field" style="left:246px;width:146px">24-01-2018</div>
  <div class="field" style="left:399px;width:92px">Select Project<svg width="8" height="8"><use href="#i-down"/></svg></div>
  <div class="field" style="left:498px;width:92px">Select Client<svg width="8" height="8"><use href="#i-down"/></svg></div>
  <div class="field" style="left:598px;width:92px">Select Tags<svg width="8" height="8"><use href="#i-down"/></svg></div>
  <div class="btn" style="left:697px;width:73px">Apply Filter</div>
  <div class="btn" style="left:776px;width:74px">Clear Filter</div>
</section>
<div class="tabs">
  <div class="tab" style="left:94px;width:60px">Yesterday</div>
  <div class="tab active" style="left:155px;width:58px">Today</div>
  <div class="tab" style="left:214px;width:60px">Tomorrow</div>
  <div class="tab" style="left:275px;width:58px">Next Week</div>
</div>
<div class="dateline">
  <svg style="position:absolute;left:11px;top:7px" width="14" height="14" viewBox="0 0 14 14"><rect x="1" y="2" width="12" height="11" fill="none" stroke="#1aaa8e" stroke-width="1.4"/><path d="M1 5h12M4 0.5v3M10 0.5v3M3.5 7.5h1.5M6.3 7.5h1.5M9 7.5h1.5M3.5 10h1.5M6.3 10h1.5M9 10h1.5" stroke="#1aaa8e" stroke-width="1.2"/></svg>
  <div class="day-label">11-Jan 2018 <small>(Thursday)</small></div>
  <div class="comment">Comment <svg width="7" height="7" viewBox="0 0 10 10"><path d="M1.5 3L5 6.5 8.5 3" stroke="#fff" stroke-width="1.8" fill="none"/></svg></div>
  <div class="stat" style="left:638px">Projects Assigned 16 of 67</div>
  <div class="stat" style="right:18px">Resoures Scheduled 8 of 55</div>
</div>

<main class="board">
<article class="block"><header class="block-head"><h3>21356-WCX HBD east -127d</h3><p class="addr">&#9679; ABC - Street, City 123456</p><svg class="gear" width="11" height="11"><use href="#i-gear"/></svg></header><div class="tag"><svg width="11" height="11"><use href="#i-tag"/></svg><span><b>Trade:</b> Shotcrete</span><svg class="x" width="6" height="6"><use href="#i-x"/></svg></div><footer class="block-foot"><svg width="13" height="13"><use href="#i-user"/></svg><svg width="13" height="13"><use href="#i-doc"/></svg><svg width="13" height="13"><use href="#i-chart"/></svg></footer></article>
<article class="block"><header class="block-head"><h3>21356-WCX HBD east -127d</h3><p class="addr">&#9679; ABC - Street, City 123456</p><svg class="gear" width="11" height="11"><use href="#i-gear"/></svg></header><div class="tag"><svg width="11" height="11"><use href="#i-tag"/></svg><span><b>Trade:</b> Shotcrete</span><svg class="x" width="6" height="6"><use href="#i-x"/></svg></div><footer class="block-foot"><svg width="13" height="13"><use href="#i-user"/></svg><svg width="13" height="13"><use href="#i-doc"/></svg><svg width="13" height="13"><use href="#i-chart"/></svg></footer></article>
<article class="block"><header class="block-head"><h3>21356-WCX HBD east -127d</h3><p class="addr">&#9679; ABC - Street, City 123456</p><svg class="gear" width="11" height="11"><use href="#i-gear"/></svg></header><div class="tag"><svg width="11" height="11"><use href="#i-tag"/></svg><span><b>Trade:</b> Shotcrete</span><svg class="x" width="6" height="6"><use href="#i-x"/></svg></div><footer class="block-foot"><svg width="13" height="13"><use href="#i-user"/></svg><svg width="13" height="13"><use href="#i-doc"/></svg><svg width="13" height="13"><use href="#i-chart"/></svg></footer></article>
<article class="block"><header class="block-head"><h3>21356-WCX HBD east -127d</h3><p class="addr">&#9679; ABC - Street, City 123456</p><svg class="gear" width="11" height="11"><use href="#i-gear"/></svg></header><div class="tag"><svg width="11" height="11"><use href="#i-tag"/></svg><span><b>Trade:</b> Shotcrete</span><svg class="x" width="6" height="6"><use href="#i-x"/></svg></div><footer class="block-foot"><svg width="13" height="13"><use href="#i-user"/></svg><svg width="13" height="13"><use href="#i-doc"/></svg><svg width="13" height="13"><use href="#i-chart"/></svg></footer></article>
<article class="block"><header class="block-head"><h3>21356-WCX HBD east -127d</h3><p class="addr">&#9679; ABC - Street, City 123456</p><svg class="gear" width="11" height="11"><use href="#i-gear"/></svg></header><div class="tag"><svg width="11" height="11"><use href="#i-tag"/></svg><span><b>Trade:</b> Shotcrete</span><svg class="x" width="6" height="6"><use href="#i-x"/></svg></div><footer class="block-foot"><svg width="13" height="13"><use href="#i-user"/></svg><svg width="13" height="13"><use href="#i-doc"/></svg><svg width="13" height="13"><use href="#i-chart"/></svg></footer></article>
<article class="block"><header class="block-head"><h3>21356-WCX HBD east -127d</h3><p class="addr">&#9679; ABC - Street, City 123456</p><svg class="gear" width="11" height="11"><use href="#i-gear"/></svg></header><div class="tag"><svg width="11" height="11"><use href="#i-tag"/></svg><span><b>Trade:</b> Shotcrete</span><svg class="x" width="6" height="6"><use href="#i-x"/></svg></div><footer class="block-foot"><svg width="13" height="13"><use href="#i-user"/></svg><svg width="13" height="13"><use href="#i-doc"/></svg><svg width="13" height="13"><use href="#i-chart"/></svg></footer></article>
<article class="block"><header class="block-head"><h3>21356-WCX HBD east -127d</h3><p class="addr">&#9679; ABC - Street, City 123456</p><svg class="gear" width="11" height="11"><use href="#i-gear"/></svg></header><div class="tag"><svg width="11" height="11"><use href="#i-tag"/></svg><span><b>Trade:</b> Shotcrete</span><svg class="x" width="6" height="6"><use href="#i-x"/></svg></div><footer class="block-foot"><svg width="13" height="13"><use href="#i-user"/></svg><svg width="13" height="13"><use href="#i-doc"/></svg><svg width="13" height="13"><use href="#i-chart"/></svg></footer></article>
<article class="block"><header class="block-head"><h3>21356-WCX HBD east -127d</h3><p class="addr">&#9679; ABC - Street, City 123456</p><svg class="gear" width="11" height="11"><use href="#i-gear"/></svg></header><div class="tag"><svg width="11" height="11"><use href="#i-tag"/></svg><span><b>Trade:</b> Shotcrete</span><svg class="x" width="6" height="6"><use href="#i-x"/></svg></div><footer class="block-foot"><svg width="13" height="13"><use href="#i-user"/></svg><svg width="13" height="13"><use href="#i-doc"/></svg><svg width="13" height="13"><use href="#i-chart"/></svg></footer></article>
<article class="block"><header class="block-head"><h3>21356-WCX HBD east -127d</h3><p class="addr">&#9679; ABC - Street, City 123456</p><svg class="gear" width="11" height="11"><use href="#i-gear"/></svg></header><div class="tag"><svg width="11" height="11"><use href="#i-tag"/></svg><span><b>Trade:</b> Shotcrete</span><svg class="x" width="6" height="6"><use href="#i-x"/></svg></div><footer class="block-foot"><svg width="13" height="13"><use href="#i-user"/></svg><svg width="13" height="13"><use href="#i-doc"/></svg><svg width="13" height="13"><use href="#i-chart"/></svg></footer></article>
<article class="block"><header class="block-head"><h3>21356-WCX HBD east -127d</h3><p class="addr">&#9679; ABC - Street, City 123456</p><svg class="gear" width="11" height="11"><use href="#i-gear"/></svg></header><div class="tag"><svg width="11" height="11"><use href="#i-tag"/></svg><span><b>Trade:</b> Shotcrete</span><svg class="x" width="6" height="6"><use href="#i-x"/></svg></div><footer class="block-foot"><svg width="13" height="13"><use href="#i-user"/></svg><svg width="13" height="13"><use href="#i-doc"/></svg><svg width="13" height="13"><use href="#i-chart"/></svg></footer></article>
<article class="block"><header class="block-head"><h3>21356-WCX HBD east -127d</h3><p class="addr">&#9679; ABC - Street, City 123456</p><svg class="gear" width="11" height="11"><use href="#i-gear"/></svg></header><div class="tag"><svg width="11" height="11"><use href="#i-tag"/></svg><span><b>Trade:</b> Shotcrete</span><svg class="x" width="6" height="6"><use href="#i-x"/></svg></div><footer class="block-foot"><svg width="13" height="13"><use href="#i-user"/></svg><svg width="13" height="13"><use href="#i-doc"/></svg><svg width="13" height="13"><use href="#i-chart"/></svg></footer></article>
<article class="block"><header class="block-head"><h3>21356-WCX HBD east -127d</h3><p class="addr">&#9679; ABC - Street, City 123456</p><svg class="gear" width="11" height="11"><use href="#i-gear"/></svg></header><div class="tag"><svg width="11" height="11"><use href="#i-tag"/></svg><span><b>Trade:</b> Shotcrete</span><svg class="x" width="6" height="6"><use href="#i-x"/></svg></div><footer class="block-foot"><svg width="13" height="13"><use href="#i-user"/></svg><svg width="13" height="13"><use href="#i-doc"/></svg><svg width="13" height="13"><use href="#i-chart"/></svg></footer></article>
<article class="block"><header class="block-head"><h3>21356-WCX HBD east -127d</h3><p class="addr">&#9679; ABC - Street, City 123456</p><svg class="gear" width="11" height="11"><use href="#i-gear"/></svg></header><div class="tag"><svg width="11" height="11"><use href="#i-tag"/></svg><span><b>Trade:</b> Shotcrete</span><svg class="x" width="6" height="6"><use href="#i-x"/></svg></div><footer class="block-foot"><svg width="13" height="13"><use href="#i-user"/></svg><svg width="13" height="13"><use href="#i-doc"/></svg><svg width="13" height="13"><use href="#i-chart"/></svg></footer></article>
<article class="block"><header class="block-head"><h3>21356-WCX HBD east -127d</h3><p class="addr">&#9679; ABC - Street, City 123456</p><svg class="gear" width="11" height="11"><use href="#i-gear"/></svg></header><div class="tag"><svg width="11" height="11"><use href="#i-tag"/></svg><span><b>Trade:</b> Shotcrete</span><svg class="x" width="6" height="6"><use href="#i-x"/></svg></div><footer class="block-foot"><svg width="13" height="13"><use href="#i-user"/></svg><svg width="13" height="13"><use href="#i-doc"/></svg><svg width="13" height="13"><use href="#i-chart"/></svg></footer></article>
<article class="block"><header class="block-head"><h3>21356-WCX HBD east -127d</h3><p class="addr">&#9679; ABC - Street, City 123456</p><svg class="gear" width="11" height="11"><use href="#i-gear"/></svg></header><div class="tag"><svg width="11" height="11"><use href="#i-tag"/></svg><span><b>Trade:</b> Shotcrete</span><svg class="x" width="6" height="6"><use href="#i-x"/></svg></div><footer class="block-foot"><svg width="13" height="13"><use href="#i-user"/></svg><svg width="13" height="13"><use href="#i-doc"/></svg><svg width="13" height="13"><use href="#i-chart"/></svg></footer></article>
<article class="block"><header class="block-head"><h3>21356-WCX HBD east -127d</h3><p class="addr">&#9679; ABC - Street, City 123456</p><svg class="gear" width="11" height="11"><use href="#i-gear"/></svg></header><div class="tag"><svg width="11" height="11"><use href="#i-tag"/></svg><span><b>Trade:</b> Shotcrete</span><svg class="x" width="6" height="6"><use href="#i-x"/></svg></div><footer class="block-foot"><svg width="13" height="13"><use href="#i-user"/></svg><svg width="13" height="13"><use href="#i-doc"/></svg><svg width="13" height="13"><use href="#i-chart"/></svg></footer></article>
<article class="block"><header class="block-head"><h3>21356-WCX HBD east -127d</h3><p class="addr">&#9679; ABC - Street, City 123456</p><svg class="gear" width="11" height="11"><use href="#i-gear"/></svg></header><div class="tag"><svg width="11" height="11"><use href="#i-tag"/></svg><span><b>Trade:</b> Shotcrete</span><svg class="x" width="6" height="6"><use href="#i-x"/></svg></div><footer class="block-foot"><svg width="13" height="13"><use href="#i-user"/></svg><svg width="13" height="13"><use href="#i-doc"/></svg><svg width="13" height="13"><use href="#i-chart"/></svg></footer></article>
<article class="block"><header class="block-head"><h3>21356-WCX HBD east -127d</h3><p class="addr">&#9679; ABC - Street, City 123456</p><svg class="gear" width="11" height="11"><use href="#i-gear"/></svg></header><div class="tag"><svg width="11" height="11"><use href="#i-tag"/></svg><span><b>Trade:</b> Shotcrete</span><svg class="x" width="6" height="6"><use href="#i-x"/></svg></div><footer class="block-foot"><svg width="13" height="13"><use href="#i-user"/></svg><svg width="13" height="13"><use href="#i-doc"/></svg><svg width="13" height="13"><use href="#i-chart"/></svg></footer></article>
<article class="block"><header class="block-head"><h3>21356-WCX HBD east -127d</h3><p class="addr">&#9679; ABC - Street, City 123456</p><svg class="gear" width="11" height="11"><use href="#i-gear"/></svg></header><div class="tag"><svg width="11" height="11"><use href="#i-tag"/></svg><span><b>Trade:</b> Shotcrete</span><svg class="x" width="6" height="6"><use href="#i-x"/></svg></div><footer class="block-foot"><svg width="13" height="13"><use href="#i-user"/></svg><svg width="13" height="13"><use href="#i-doc"/></svg><svg width="13" height="13"><use href="#i-chart"/></svg></footer></article>
<article class="block"><header class="block-head"><h3>21356-WCX HBD east -127d</h3><p class="addr">&#9679; ABC - Street, City 123456</p><svg class="gear" width="11" height="11"><use href="#i-gear"/></svg></header><div class="tag"><svg width="11" height="11"><use href="#i-tag"/></svg><span><b>Trade:</b> Shotcrete</span><svg class="x" width="6" height="6"><use href="#i-x"/></svg></div><footer class="block-foot"><svg width="13" height="13"><use href="#i-user"/></svg><svg width="13" height="13"><use href="#i-doc"/></svg><svg width="13" height="13"><use href="#i-chart"/></svg></footer></article>
<article class="block"><header class="block-head"><h3>21356-WCX HBD east -127d</h3><p class="addr">&#9679; ABC - Street, City 123456</p><svg class="gear" width="11" height="11"><use href="#i-gear"/></svg></header><div class="tag"><svg width="11" height="11"><use href="#i-tag"/></svg><span><b>Trade:</b> Shotcrete</span><svg class="x" width="6" height="6"><use href="#i-x"/></svg></div><footer class="block-foot"><svg width="13" height="13"><use href="#i-user"/></svg><svg width="13" height="13"><use href="#i-doc"/></svg><svg width="13" height="13"><use href="#i-chart"/></svg></footer></article>
<article class="block"><header class="block-head"><h3>21356-WCX HBD east -127d</h3><p class="addr">&#9679; ABC - Street, City 123456</p><svg class="gear" width="11" height="11"><use href="#i-gear"/></svg></header><div class="tag"><svg width="11" height="11"><use href="#i-tag"/></svg><span><b>Trade:</b> Shotcrete</span><svg class="x" width="6" height="6"><use href="#i-x"/></svg></div><footer class="block-foot"><svg width="13" height="13"><use href="#i-user"/></svg><svg width="13" height="13"><use href="#i-doc"/></svg><svg width="13" height="13"><use href="#i-chart"/></svg></footer></article>
<article class="block"><header class="block-head"><h3>21356-WCX HBD east -127d</h3><p class="addr">&#9679; ABC - Street, City 123456</p><svg class="gear" width="11" height="11"><use href="#i-gear"/></svg></header><div class="tag"><svg width="11" height="11"><use href="#i-tag"/></svg><span><b>Trade:</b> Shotcrete</span><svg class="x" width="6" height="6"><use href="#i-x"/></svg></div><footer class="block-foot"><svg width="13" height="13"><use href="#i-user"/></svg><svg width="13" height="13"><use href="#i-doc"/></svg><svg width="13" height="13"><use href="#i-chart"/></svg></footer></article>
<article class="block"><header class="block-head"><h3>21356-WCX HBD east -127d</h3><p class="addr">&#9679; ABC - Street, City 123456</p><svg class="gear" width="11" height="11"><use href="#i-gear"/></svg></header><div class="tag"><svg width="11" height="11"><use href="#i-tag"/></svg><span><b>Trade:</b> Shotcrete</span><svg class="x" width="6" height="6"><use href="#i-x"/></svg></div><footer class="block-foot"><svg width="13" height="13"><use href="#i-user"/></svg><svg width="13" height="13"><use href="#i-doc"/></svg><svg width="13" height="13"><use href="#i-chart"/></svg></footer></article>
<article class="block"><header class="block-head"><h3>21356-WCX HBD east -127d</h3><p class="addr">&#9679; ABC - Street, City 123456</p><svg class="gear" width="11" height="11"><use href="#i-gear"/></svg></header><div class="tag"><svg width="11" height="11"><use href="#i-tag"/></svg><span><b>Trade:</b> Shotcrete</span><svg class="x" width="6" height="6"><use href="#i-x"/></svg></div><footer class="block-foot"><svg width="13" height="13"><use href="#i-user"/></svg><svg width="13" height="13"><use href="#i-doc"/></svg><svg width="13" height="13"><use href="#i-chart"/></svg></footer></article>
<article class="block"><header class="block-head"><h3>21356-WCX HBD east -127d</h3><p class="addr">&#9679; ABC - Street, City 123456</p><svg class="gear" width="11" height="11"><use href="#i-gear"/></svg></header><div class="tag"><svg width="11" height="11"><use href="#i-tag"/></svg><span><b>Trade:</b> Shotcrete</span><svg class="x" width="6" height="6"><use href="#i-x"/></svg></div><footer class="block-foot"><svg width="13" height="13"><use href="#i-user"/></svg><svg width="13" height="13"><use href="#i-doc"/></svg><svg width="13" height="13"><use href="#i-chart"/></svg></footer></article>
<article class="block"><header class="block-head"><h3>21356-WCX HBD east -127d</h3><p class="addr">&#9679; ABC - Street, City 123456</p><svg class="gear" width="11" height="11"><use href="#i-gear"/></svg></header><div class="tag"><svg width="11" height="11"><use href="#i-tag"/></svg><span><b>Trade:</b> Shotcrete</span><svg class="x" width="6" height="6"><use href="#i-x"/></svg></div><footer class="block-foot"><svg width="13" height="13"><use href="#i-user"/></svg><svg width="13" height="13"><use href="#i-doc"/></svg><svg width="13" height="13"><use href="#i-chart"/></svg></footer></article>
<article class="block"><header class="block-head"><h3>21356-WCX HBD east -127d</h3><p class="addr">&#9679; ABC - Street, City 123456</p><svg class="gear" width="11" height="11"><use href="#i-gear"/></svg></header><div class="tag"><svg width="11" height="11"><use href="#i-tag"/></svg><span><b>Trade:</b> Shotcrete</span><svg class="x" width="6" height="6"><use href="#i-x"/></svg></div><footer class="block-foot"><svg width="13" height="13"><use href="#i-user"/></svg><svg width="13" height="13"><use href="#i-doc"/></svg><svg width="13" height="13"><use href="#i-chart"/></svg></footer></article>
<article class="block"><header class="block-head"><h3>21356-WCX HBD east -127d</h3><p class="addr">&#9679; ABC - Street, City 123456</p><svg class="gear" width="11" height="11"><use href="#i-gear"/></svg></header><div class="tag"><svg width="11" height="11"><use href="#i-tag"/></svg><span><b>Trade:</b> Shotcrete</span><svg class="x" width="6" height="6"><use href="#i-x"/></svg></div><footer class="block-foot"><svg width="13" height="13"><use href="#i-user"/></svg><svg width="13" height="13"><use href="#i-doc"/></svg><svg width="13" height="13"><use href="#i-chart"/></svg></footer></article>
<article class="block"><header class="block-head"><h3>21356-WCX HBD east -127d</h3><p class="addr">&#9679; ABC - Street, City 123456</p><svg class="gear" width="11" height="11"><use href="#i-gear"/></svg></header><div class="tag"><svg width="11" height="11"><use href="#i-tag"/></svg><span><b>Trade:</b> Shotcrete</span><svg class="x" width="6" height="6"><use href="#i-x"/></svg></div><footer class="block-foot"><svg width="13" height="13"><use href="#i-user"/></svg><svg width="13" height="13"><use href="#i-doc"/></svg><svg width="13" height="13"><use href="#i-chart"/></svg></footer></article>
<article class="block"><header class="block-head"><h3>21356-WCX HBD east -127d</h3><p class="addr">&#9679; ABC - Street, City 123456</p><svg class="gear" width="11" height="11"><use href="#i-gear"/></svg></header><div class="tag"><svg width="11" height="11"><use href="#i-tag"/></svg><span><b>Trade:</b> Shotcrete</span><svg class="x" width="6" height="6"><use href="#i-x"/></svg></div><footer class="block-foot"><svg width="13" height="13"><use href="#i-user"/></svg><svg width="13" height="13"><use href="#i-doc"/></svg><svg width="13" height="13"><use href="#i-chart"/></svg></footer></article>
<article class="block"><header class="block-head"><h3>21356-WCX HBD east -127d</h3><p class="addr">&#9679; ABC - Street, City 123456</p><svg class="gear" width="11" height="11"><use href="#i-gear"/></svg></header><div class="tag"><svg width="11" height="11"><use href="#i-tag"/></svg><span><b>Trade:</b> Shotcrete</span><svg class="x" width="6" height="6"><use href="#i-x"/></svg></div><footer class="block-foot"><svg width="13" height="13"><use href="#i-user"/></svg><svg width="13" height="13"><use href="#i-doc"/></svg><svg width="13" height="13"><use href="#i-chart"/></svg></footer></article>
</main>
</body>
</html>
```